Business Card + Stationery Design for a Craft Beer Bar

Mr. Tovell's is a taproom sport bar that contains in its menu beers from different places around the world. What we offer differently is the experience that you can get inside our location, ambient music with rock from the 80s to 90s, projection with the sports of the moment, board games and private events.

Target Market(s)

Young people, Mid and High Class

Industry/Entity Type

Business

Font styles to use
Serif
Sans Serif

Colors
fee18a

Requirements
Must have
• Name, Title, Contact Details, Website
Nice to have
• Mail Signature
Should not have
• n/a

```html
<!DOCTYPE html>
<html lang="en">
<head>
<meta charset="utf-8">
<title>Mr. Tovell's – Business Cards</title>
<link rel="stylesheet" href="https://fonts.googleapis.com/css2?family=Oswald:wght@400;500&display=swap">
<style>
  :root {
    --stage: #2a2a2c;
    --gold: #f2bc57;
    --ink: #1c181c;
    --paper: #ffffff;
    --mist: #eceded;
    --rule: #4a4a4a;
  }
  * { margin: 0; padding: 0; box-sizing: border-box; }
  html, body { width: 1200px; height: 900px; overflow: hidden; }
  body {
    background: var(--stage);
    font-family: "Oswald", "Arial Narrow", sans-serif;
    font-weight: 500;
    position: relative;
  }
  .card {
    position: absolute;
    width: 514px;
    height: 297px;
    overflow: hidden;
  }
  .card--gold   { left: 72px;  top: 138px; background: var(--gold); }
  .card--dark   { left: 615px; top: 138px; background: var(--ink); }
  .card--split  { left: 72px;  top: 463px; background: var(--paper); }
  .card--center { left: 615px; top: 463px; background: var(--paper); }

  .wordmark {
    display: flex; align-items: center; justify-content: center; gap: 9px;
    font-weight: 400; font-size: 26px; line-height: 1; letter-spacing: 0;
  }
  .wordmark__dot { width: 10px; height: 10px; border-radius: 50%; flex: none; }

  .card--gold .wordmark, .card--dark .wordmark {
    position: absolute; left: 0; right: 0; top: 137px;
  }
  .card--gold .wordmark { color: var(--ink); }
  .card--gold .wordmark__dot { background: var(--ink); }
  .card--dark .wordmark { color: var(--paper); }
  .card--dark .wordmark__dot { background: var(--gold); }

  .site {
    position: absolute; left: 0; right: 0; top: 252px;
    text-align: center; font-size: 13px; letter-spacing: 0.4px;
  }
  .card--gold .site { color: var(--ink); }
  .card--dark .site { color: var(--gold); }

  .person__name { font-size: 19px; line-height: 1.1; text-transform: uppercase; }
  .person__role { font-size: 12px; color: var(--gold); margin-top: 3px; letter-spacing: 0.4px; }
  .contact { position: absolute; color: var(--ink); }
  .contact__lines { font-size: 12px; line-height: 17px; }

  /* split card */
  .card--split .wordmark {
    position: absolute; left: 20px; width: 226px; top: 171px; color: var(--ink);
  }
  .card--split .wordmark__dot { background: var(--gold); }
  .card--split .divider {
    position: absolute; left: 257px; top: 60px; width: 2px; height: 179px;
    background: var(--rule);
  }
  .card--split .contact { left: 308px; top: 80px; }
  .card--split .contact__phone { margin-top: 12px; }
  .card--split .contact__address { margin-top: 12px; }

  /* centered card */
  .character-shade {
    position: absolute; left: 0; top: 0; width: 160px; height: 297px;
    background: linear-gradient(90deg, var(--mist) 0%, rgba(236,237,237,0.55) 70%, rgba(236,237,237,0) 100%);
  }
  .card--center .wordmark {
    position: absolute; left: 150px; width: 212px; top: 118px; color: var(--ink);
  }
  .card--center .wordmark__dot { background: var(--gold); }
  .card--center .person {
    position: absolute; right: 277px; top: 212px; text-align: right; color: var(--ink);
  }
  .card--center .divider {
    position: absolute; left: 249px; top: 187px; width: 1px; height: 90px;
    background: var(--gold);
  }
  .card--center .contact { left: 262px; top: 192px; }
  .card--center .contact__address { margin-top: 8px; }
</style>
</head>
<body>
  <section class="card card--gold" aria-label="Card front, gold">
    <div class="wordmark"><span class="wordmark__dot"></span>Mr. Tovell's</div>
    <p class="site">TOVELLTAPS.COM</p>
  </section>

  <section class="card card--dark" aria-label="Card front, dark">
    <div class="wordmark"><span class="wordmark__dot"></span>Mr. Tovell's</div>
    <p class="site">TOVELLTAPS.COM</p>
  </section>

  <section class="card card--split" aria-label="Card back, split layout">
    <div class="wordmark"><span class="wordmark__dot"></span>Mr. Tovell's</div>
    <span class="divider"></span>
    <div class="contact">
      <div class="person">
        <p class="person__name">Daniel Harrow</p>
        <p class="person__role">OWNER</p>
      </div>
      <div class="contact__lines contact__phone">
        <p>5550 284 917</p>
        <p>D.HARROW@TOVELLTAPS.COM</p>
      </div>
      <div class="contact__lines contact__address">
        <p>48 MAPLE ROW</p>
        <p>LAKEVIEW, NEW YORK 14002</p>
      </div>
    </div>
  </section>

  <section class="card card--center" aria-label="Card back, centered layout">
    <div class="character-shade" role="img" aria-label="Large faint brand character illustration"></div>
    <div class="wordmark"><span class="wordmark__dot"></span>Mr. Tovell's</div>
    <div class="person">
      <p class="person__name">Daniel Harrow</p>
      <p class="person__role">OWNER</p>
    </div>
    <span class="divider"></span>
    <div class="contact">
      <div class="contact__lines">
        <p>5550 284 917</p>
        <p>D.HARROW@TOVELLTAPS.COM</p>
      </div>
      <div class="contact__lines contact__address">
        <p>48 MAPLE ROW</p>
        <p>LAKEVIEW, NEW YORK 14002</p>
      </div>
    </div>
  </section>
</body>
</html>
```